Womans Supplement Designs

Launching a Supplement company and need to get some initial designs created, I've attached our logo and the bottle type that I want the samples done one.

This project is for our Whey Protein we are starting with Vanilla, chocolate and strawberry banana

(ALL DESIGN VARIATIONS MUST BE A WHITE BOTTLE NOT BLACK)

(FOR DESIGN SAMPLES PLEASE USE THE SUPPLEMENT BOTTLE STYLE I PROVIDED)

Whoever is selected the winner I will have more work for you to complete the disigns for the rest of the products in the line, Just want to get this shake completed first

Target Market(s)

Women

Requirements
Must have
• Must have our current logo involved

the name of this product will be "KIVA LUM"

Must have this slogan,

ALL-IN-ONE PREMIUM PROTEIN NUTRITIONAL SHAKE FOR BLACK WOMEN

This is our meal replacement

the design should try to keep the same look and feel of the existing provided supplement images

we are starting with chocolate, vanilla and strawberry banana

this is for women and should look colorful and appeal to them
Should not have
• Do not use an image of a person or lady, don't want it branded to a person

```html
<!DOCTYPE html>
<html lang="en">
<head>
<meta charset="utf-8">
<title>Kiva Lum – Chocolate Label</title>
<link rel="stylesheet" href="https://fonts.googleapis.com/css2?family=Exo+2:wght@500;600&family=Roboto+Condensed:wght@400&display=swap">
<style>
  :root {
    --backdrop: #dec5a6;
    --label-white: #ffffff;
    --ink-dark: #2e2522;
    --brand-ink: #3a2a22;
    --cocoa: #7d4a2e;
    --cocoa-deep: #7a3a06;
    --bronze: #c99a5e;
    --title-brown: #8a3f0e;
    --flavour-white: #ffffff;
  }
  * { margin: 0; padding: 0; box-sizing: border-box; }
  html, body {
    width: 940px;
    height: 1200px;
    overflow: hidden;
    background: var(--backdrop);
  }
  .canvas {
    position: relative;
    width: 940px;
    height: 1200px;
    background: var(--backdrop);
  }
  .label {
    position: absolute;
    left: 40px;
    top: 287px;
    width: 860px;
    height: 626px;
    background: var(--label-white);
    overflow: hidden;
  }
  .label-band {
    position: absolute;
    inset: 0;
    width: 860px;
    height: 626px;
  }
  .brand {
    position: absolute;
    top: 40px;
    left: 0;
    width: 100%;
    display: flex;
    justify-content: center;
    align-items: center;
    gap: 12px;
  }
  .brand-mark {
    width: 18px;
    height: 18px;
    background: var(--cocoa-deep);
  }
  .brand-name {
    font-family: "Exo 2", sans-serif;
    font-weight: 600;
    font-size: 20px;
    letter-spacing: 0.18em;
    color: var(--brand-ink);
  }
  .product-name {
    position: absolute;
    top: 152px;
    left: 0;
    width: 100%;
    text-align: center;
    font-family: "Exo 2", sans-serif;
    font-weight: 500;
    font-size: 64px;
    line-height: 1;
    letter-spacing: 0.02em;
    color: var(--title-brown);
  }
  .slogan {
    position: absolute;
    top: 262px;
    left: 0;
    width: 100%;
    text-align: center;
    font-family: "Roboto Condensed", sans-serif;
    font-weight: 400;
    color: var(--ink-dark);
    line-height: 1;
  }
  .slogan-top { font-size: 17px; display: block; }
  .slogan-main { font-size: 30px; display: block; margin-top: 11px; }
  .slogan-bottom { font-size: 18px; display: block; margin-top: 8px; }
  .flavour {
    position: absolute;
    top: 553px;
    left: 0;
    width: 100%;
    text-align: center;
    font-family: "Exo 2", sans-serif;
    font-weight: 500;
    font-size: 27px;
    letter-spacing: 0.04em;
    color: var(--flavour-white);
  }
</style>
</head>
<body>
<main class="canvas">
  <section class="label">
    <svg class="label-band" viewBox="0 0 860 626" aria-hidden="true">
      <defs>
        <linearGradient id="band-metal" x1="0" y1="0" x2="1" y2="0">
          <stop offset="0" stop-color="var(--cocoa)"/>
          <stop offset="0.24" stop-color="var(--bronze)"/>
          <stop offset="0.46" stop-color="var(--cocoa-deep)"/>
          <stop offset="0.55" stop-color="var(--cocoa-deep)"/>
          <stop offset="0.76" stop-color="var(--bronze)"/>
          <stop offset="1" stop-color="var(--cocoa)"/>
        </linearGradient>
        <linearGradient id="frame-metal" x1="0" y1="0" x2="1" y2="0">
          <stop offset="0" stop-color="var(--bronze)"/>
          <stop offset="0.3" stop-color="var(--cocoa-deep)"/>
          <stop offset="0.5" stop-color="var(--bronze)"/>
          <stop offset="0.7" stop-color="var(--cocoa-deep)"/>
          <stop offset="1" stop-color="var(--bronze)"/>
        </linearGradient>
      </defs>
      <path d="M0 146 L431 501 L860 146 L860 626 L0 626 Z" fill="url(#band-metal)"/>
      <path d="M20 189 L431 527 L840 184 L840 600 L20 600 Z" fill="none" stroke="url(#frame-metal)" stroke-width="5"/>
    </svg>

    <div class="brand">
      <span class="brand-mark"></span>
      <span class="brand-name">SABLE GRACE</span>
    </div>

    <h1 class="product-name">KIVA LUM</h1>

    <p class="slogan">
      <span class="slogan-top">ALL-IN-ONE PREMIUM</span>
      <span class="slogan-main">PROTEIN NUTRITIONAL</span>
      <span class="slogan-bottom">SHAKE FOR BLACK WOMEN</span>
    </p>

    <p class="flavour">CHOCOLATE</p>
  </section>
</main>
</body>
</html>
```